Varlen Group Business Card design with current logo

hello all , we have abranded logo which i will attach but we need a card double sided designed . one side is easy as its the logo but the other side we want clean and modern. The info needed will be the same text as the card sample attached. no pictures of us though just clean and professinal pls. Logo can be incorporated on the text side to for recognition. Colors are Black , white , red and grey... ideal card would be matt finish high end stock. or a black card so white text ... Sorry i have uploaded al the files i got when I had the logo designed on here.. Oh forgot want to say pls add in the card details EST 1981 and over 40yrs combined experiance
Updates

Hello everyone , I'm really sorry we haven't been able to make a final decision.. There is at least 3 cards that all have there positives over the other two... We will decide by tonight.

Target Market(s)

20-70 wide range but people with money and a education.

Industry/Entity Type

Real Estate Agent

Contact Information for Business Card

One side the Logo choose from the different color logos, black being the one we like most, other side is the details. Clean professional looking fonts. EST 1981 , over 40yrs experiance. Website email and both names and PH# as per the sample card attached

Font styles to use
Other font styles liked:
• Fonts:Code Bold,Code Light, Lucida Fax.

Colors
1b1b1b
757575
c9c9c9
e8e8e8
ffffff
e9e9e9

Requirements
Must have
• Logo and contact info

```html
<!DOCTYPE html>
<html lang="en">
<head>
<meta charset="UTF-8">
<title>Varlen Group – Business Card</title>
<link rel="stylesheet" href="https://fonts.googleapis.com/css2?family=Lato:wght@400&family=Raleway:wght@400&display=swap">
<style>
  :root {
    --backdrop: #1b1b1b;
    --card: #2f3034;
    --brand-red: #8c1b1e;
    --text-light: #c9c9c9;
    --text-white: #ffffff;
  }
  * { margin: 0; padding: 0; box-sizing: border-box; }
  html, body {
    width: 1200px;
    height: 900px;
    overflow: hidden;
    background: var(--backdrop);
  }
  .canvas {
    position: relative;
    width: 1200px;
    height: 900px;
    background: var(--backdrop);
  }
  .card {
    position: absolute;
    left: 331px;
    width: 542px;
    height: 315px;
    border-radius: 16px;
    background: var(--card);
  }
  .card--front { top: 121px; }
  .card--back { top: 489px; }

  .brand-mark {
    display: block;
    background: var(--brand-red);
  }

  /* Front: details side */
  .front-brand {
    position: absolute;
    left: 85px;
    top: 110px;
    display: flex;
    flex-direction: column;
    gap: 12px;
  }
  .front-brand .brand-mark { width: 64px; height: 64px; }
  .front-brand .brand-name {
    font-family: "Raleway", sans-serif;
    font-weight: 400;
    font-size: 17px;
    color: var(--brand-red);
  }
  .contact {
    position: absolute;
    left: 281px;
    top: 116px;
    font-family: "Raleway", sans-serif;
    font-weight: 400;
  }
  .contact__name {
    font-size: 25px;
    line-height: 1;
    color: var(--brand-red);
  }
  .contact__role {
    margin-top: 3px;
    font-size: 16px;
    color: var(--text-light);
  }
  .contact__lines {
    margin-top: 22px;
    margin-left: 3px;
    font-size: 14px;
    line-height: 19px;
    color: var(--text-light);
  }

  /* Back: logo side */
  .back-brand {
    position: absolute;
    left: 0;
    right: 0;
    top: 99px;
    display: flex;
    justify-content: center;
    align-items: center;
    gap: 18px;
  }
  .back-brand .brand-mark { width: 100px; height: 100px; }
  .back-brand .brand-name {
    font-family: "Raleway", sans-serif;
    font-weight: 400;
    font-size: 40px;
    color: var(--brand-red);
  }
  .tagline {
    position: absolute;
    left: 0;
    right: 0;
    top: 259px;
    text-align: center;
    font-family: "Lato", sans-serif;
    font-weight: 400;
    font-size: 16px;
    color: var(--text-white);
  }
</style>
</head>
<body>
<main class="canvas">
  <section class="card card--front" aria-label="Card details side">
    <div class="front-brand">
      <span class="brand-mark"></span>
      <span class="brand-name">Varlen Group</span>
    </div>
    <div class="contact">
      <p class="contact__name">Daniel Marsh</p>
      <p class="contact__role">Managing Director</p>
      <p class="contact__lines">hello@varlengroup.com<br>044-987 654 321</p>
    </div>
  </section>

  <section class="card card--back" aria-label="Card brand side">
    <div class="back-brand">
      <span class="brand-mark"></span>
      <span class="brand-name">Varlen Group</span>
    </div>
    <p class="tagline">EST 1981 and over 40yrs combined experiance</p>
  </section>
</main>
</body>
</html>
```